Brantley Estates is a commercial real estate development company based in the United States. We develop high-end office buildings and student housing apartments. We have a new logo and need to update all of our stationary items and business cards. We would like the design to be clean and professional. Our logo and color information is attached. Our logo MUST be in full color and not as white. It is preferred that the logo is on a white background.

Color code Blue R 0. G 62. B 124 ( #003E7C )
C 100 M84 Y 26 K 22
Black R32. G30. B30 ( #201E1E)
C100 M100 Y100 K100

Font used TRAJAN PRO3 PRO BOLD.

Items needed:
1. Business card - Leaning towards doing just a one side business card in a thicker paper. Include - logo, name - Martin E. Caldwell, Title - Chairman & CEO, 5120 Ridgemont Pkwy. Suite 400, Atlanta, GA 30327 - Cell number 404.617.####, Office 770.245.62## email@brantleyestates.com; www.brantleyestates.com.

2. Letterhead - Standard 8.5 by 11 paper. We do have a smaller size for the CEO that is 7.25 by 10.5 that is just a mirror of the letterhead except with his name (Martin E. Caldwell) and title (Chariman & CEO) listed at the top in the header. Letthead needs address, phone number and website, plus logo. *Prepared such that we can either implement as a Google Document template or professionally print.

3. Legal sized envelope - #10 envelope - which measures 4 1/8" by 9 1/2". We also use the same size envelope with a window. Need logo and address. A photo of the old envelope style is attached.

4. 9" x 12" Pocket folder - Need a design that can also be split to be a cover page and back - We use the cover pages in spiral binding machine, so we need to leave room on the left for that. One of the pockets should hold a business card. Include logo, address, phone, website. Also if text is needed, we could say development / leasing / property management.

5. Shipping label - 3 1/3" x 4" inches and 6 per page. Just need logo and address listed at top of the label and white space at bottom.

Company: Brantley Estates
Address: 5120 Ridgemont Pkwy. Suite 400, Atlanta, GA 30327
Phone: 770.245.6274
Fax: 770.245.6219 (probably not needed)
Website: www.brantleyestates.com

Thank you for all your help!

Target Market(s)

Should communicate a strong corporate feel

Contact Information for Business Card

Include - logo, name - Martin E. Caldwell, Title - Chairman & CEO, 5120 Ridgemont Pkwy. Suite 400, Atlanta, GA 30327 - Cell number 404.617.####, Office 770.245.62## email@brantleyestates.com; www.brantleyestates.com.

Logo Text

Brantley Estates

Colors

Designer to choose colors to be used in the design.

Requirements
Must have
• Our logo MUST be in full color and not as white. It is preferred that the logo is on a white background.
• Colors - Color code Blue R 0. G 62. B 124 ( #003E7C )
• C 100 M84 Y 26 K 22
Nice to have
• Font used in logo TRAJAN PRO3 PRO BOLD. Would love to see options of both a one sided and double-sided.
Should not have
• Logo in white.

```html
<!DOCTYPE html>
<html lang="en">
<head>
<meta charset="utf-8">
<title>Brantley Estates – Stationery</title>
<link href="https://fonts.googleapis.com/css2?family=Cinzel:wght@700&family=Lato:wght@400;700&family=Arimo:wght@400;700&display=swap" rel="stylesheet">
<style>
  :root{
    --navy:#14366b;
    --ink:#201e1e;
    --paper:#f4f4f4;
    --copy:#6d6d6d;
    --stage:#e6e4e1;
  }
  *{margin:0;padding:0;box-sizing:border-box}
  html,body{width:1200px;height:1200px;overflow:hidden;background:var(--stage)}
  .canvas{position:relative;width:1200px;height:1200px}

  .brand{position:absolute;display:flex;align-items:center;color:var(--navy);font-family:"Cinzel",serif;font-weight:700}
  .brand__dot{border-radius:50%;background:var(--navy);flex:none}
  .brand__name{line-height:1}
  .brand__name span{display:block}

  /* Business card */
  .card{position:absolute;left:54px;width:304px;height:174px;background:var(--paper);overflow:hidden;box-shadow:0 3px 6px rgba(0,0,0,.35)}
  .card--a{top:136px}
  .card--b{top:336px}
  .card__wave{position:absolute;inset:0}
  .card .brand{left:23px;top:20px}
  .card .brand__dot{width:26px;height:26px;margin-right:8px}
  .card .brand__name span:first-child{font-size:17px;letter-spacing:.5px}
  .card .brand__name span:last-child{font-size:8.5px;letter-spacing:2.6px;margin-top:2px}
  .card__person{position:absolute;left:23px;top:78px;color:var(--navy)}
  .card__name{font-family:"Cinzel",serif;font-weight:700;font-size:10.5px;letter-spacing:.3px}
  .card__title{font-family:"Lato",sans-serif;font-size:7px;color:#333;margin-top:-1px}
  .card__address{position:absolute;left:23px;top:138px;font-family:"Lato",sans-serif;font-size:7px;line-height:9px;color:#fff}
  .card__contacts{position:absolute;right:22px;top:121px;list-style:none;font-family:"Lato",sans-serif;font-size:7px;line-height:8.5px;color:#fff;text-align:right}
  .card__contacts li{display:flex;justify-content:flex-end;align-items:center;gap:5px}
  .card__contacts svg{width:6px;height:6px;flex:none}

  /* Letterhead */
  .letterhead{position:absolute;left:401px;top:122px;width:735px;height:952px;background:var(--paper);overflow:hidden;box-shadow:0 4px 10px rgba(0,0,0,.3)}
  .letterhead__wave{position:absolute;inset:0}
  .letterhead .brand{left:51px;top:44px}
  .letterhead .brand__dot{width:58px;height:58px;margin-right:16px}
  .letterhead .brand__name span:first-child{font-size:36px;letter-spacing:1px}
  .letterhead .brand__name span:last-child{font-size:16px;letter-spacing:6.4px;margin-top:6px}
  .letterhead__contact{position:absolute;left:510px;top:44px;font-family:"Lato",sans-serif;font-size:12.5px;line-height:15px;color:#222}
  .letterhead__contact ul{list-style:none;margin-top:5px}
  .letterhead__contact li{display:flex;align-items:center;gap:8px}
  .letterhead__contact svg{width:9px;height:9px;flex:none}
  .letter{position:absolute;left:86px;width:580px;font-family:"Arimo",sans-serif;font-size:11.8px;line-height:16.8px;color:var(--copy)}
  .letter strong{font-weight:700}
  .letter--date{top:227px}
  .letter--recipient{top:261px}
  .letter--greeting{top:362px}
  .letter--body{top:395px}
  .letter--body p{margin-bottom:16.8px}
  .letter--closing{top:715px}
  .letter__signature{display:block;width:250px;height:30px;margin:4px 0 2px -8px;background:linear-gradient(90deg,rgba(40,40,40,.18),rgba(40,40,40,.05));border-radius:3px}
  .letterhead__web{position:absolute;right:67px;top:906px;font-family:"Lato",sans-serif;font-size:12.5px;color:#fff}
  .letterhead__web b{font-weight:700}
</style>
</head>
<body>
<div class="canvas">

  <!-- Business card, front -->
  <section class="card card--a" aria-label="Business card">
    <svg class="card__wave" viewBox="0 0 304 174" preserveAspectRatio="none">
      <path d="M110 120 Q220 110 304 54 L304 66 Q215 113 110 120Z" fill="var(--ink)"/>
      <path d="M0 120 Q185 119 304 74 L304 174 L0 174Z" fill="var(--navy)"/>
    </svg>
    <div class="brand"><span class="brand__dot"></span><div class="brand__name"><span>BRANTLEY</span><span>ESTATES</span></div></div>
    <div class="card__person"><div class="card__name">Martin E. Caldwell</div><div class="card__title">Chairman &amp; CEO</div></div>
    <div class="card__address">5120 Ridgemont Pkwy.<br>Suite 400, Atlanta, GA 30327</div>
    <ul class="card__contacts">
      <li>404.617.#### <svg viewBox="0 0 10 10"><rect x="2.5" y="0.5" width="5" height="9" rx="1" fill="none" stroke="#fff"/></svg></li>
      <li>770.245.62## <svg viewBox="0 0 10 10"><path d="M2 1 L4 1 L5 3 L4 4 Q5 6 6 6 L7 5 L9 6 L9 8 Q5 9 2 5 Q1 3 2 1Z" fill="#fff"/></svg></li>
      <li>email@brantleyestates.com <svg viewBox="0 0 10 10"><rect x="0.5" y="2" width="9" height="6" fill="none" stroke="#fff"/><path d="M0.5 2 L5 5.5 L9.5 2" fill="none" stroke="#fff"/></svg></li>
      <li>www.brantleyestates.com <svg viewBox="0 0 10 10"><circle cx="5" cy="5" r="4.5" fill="#fff"/></svg></li>
    </ul>
  </section>

  <!-- Business card, second -->
  <section class="card card--b" aria-label="Business card">
    <svg class="card__wave" viewBox="0 0 304 174" preserveAspectRatio="none">
      <path d="M110 120 Q220 110 304 54 L304 66 Q215 113 110 120Z" fill="var(--ink)"/>
      <path d="M0 120 Q185 119 304 74 L304 174 L0 174Z" fill="var(--navy)"/>
    </svg>
    <div class="brand"><span class="brand__dot"></span><div class="brand__name"><span>BRANTLEY</span><span>ESTATES</span></div></div>
    <div class="card__person"><div class="card__name">Martin E. Caldwell</div><div class="card__title">Chairman &amp; CEO</div></div>
    <div class="card__address">5120 Ridgemont Pkwy.<br>Suite 400, Atlanta, GA 30327</div>
    <ul class="card__contacts">
      <li>404.617.#### <svg viewBox="0 0 10 10"><rect x="2.5" y="0.5" width="5" height="9" rx="1" fill="none" stroke="#fff"/></svg></li>
      <li>770.245.62## <svg viewBox="0 0 10 10"><path d="M2 1 L4 1 L5 3 L4 4 Q5 6 6 6 L7 5 L9 6 L9 8 Q5 9 2 5 Q1 3 2 1Z" fill="#fff"/></svg></li>
      <li>email@brantleyestates.com <svg viewBox="0 0 10 10"><rect x="0.5" y="2" width="9" height="6" fill="none" stroke="#fff"/><path d="M0.5 2 L5 5.5 L9.5 2" fill="none" stroke="#fff"/></svg></li>
      <li>www.brantleyestates.com <svg viewBox="0 0 10 10"><circle cx="5" cy="5" r="4.5" fill="#fff"/></svg></li>
    </ul>
  </section>

  <!-- Letterhead -->
  <section class="letterhead" aria-label="Letterhead">
    <svg class="letterhead__wave" viewBox="0 0 735 952" preserveAspectRatio="none">
      <path d="M130 926 Q500 902 735 810 L735 830 Q510 912 130 926Z" fill="var(--ink)"/>
      <path d="M0 940 Q480 932 735 842 L735 952 L0 952Z" fill="var(--navy)"/>
    </svg>
    <div class="brand"><span class="brand__dot"></span><div class="brand__name"><span>BRANTLEY</span><span>ESTATES</span></div></div>
    <div class="letterhead__contact">
      5120 Ridgemont Pkwy.<br>Suite 400, Atlanta, GA 30327
      <ul>
        <li><svg viewBox="0 0 10 10"><rect x="2.5" y="0.5" width="5" height="9" rx="1" fill="none" stroke="var(--navy)" stroke-width="1.2"/></svg>404.617.####</li>
        <li><svg viewBox="0 0 10 10"><path d="M2 1 L4 1 L5 3 L4 4 Q5 6 6 6 L7 5 L9 6 L9 8 Q5 9 2 5 Q1 3 2 1Z" fill="var(--navy)"/></svg>770.245.62##</li>
        <li><svg viewBox="0 0 10 10"><rect x="0.5" y="2" width="9" height="6" fill="none" stroke="var(--navy)"/><path d="M0.5 2 L5 5.5 L9.5 2" fill="none" stroke="var(--navy)"/></svg>email@brantleyestates.com</li>
      </ul>
    </div>

    <div class="letter letter--date">January 1, 2050</div>
    <div class="letter letter--recipient"><strong>Daniel Reeves</strong><br>Managing Director<br>Co.Street, Building/Suite<br>City/State, Zip Code</div>
    <div class="letter letter--greeting">Dear Thomas Whitfield,</div>
    <div class="letter letter--body">
      <p>Lorem ipsum dolor sit amet, consectetuer adipiscing elit, sed diam nonummy nibh euismod tincidunt ut laoreet dolore magna aliquam erat volutpat. Ut wisi enim ad minim veniam, quis nostrud exerci tation ullamcorper suscipit lobortis nisl ut aliquip ex ea commodo consequat. Duis dolore te feugait nulla facilisi. Nam liber tempor cum soluta nobis eleifend option congue nihil imperdiet doming id quod mazim placerat facer possim assum. Lorem ipsum dolor sit amet, consectetuer adipiscing elit, sed diam nonummy nibh euismod tincidunt ut laoreet dolore magna aliquam erat volutpat. Ut wisi enim ad minim veniam, quis nostrud exerci tation ullamcorper suscipit lobortis nisl ut aliquip ex ea commodo consequat.</p>
      <p>Consectetuer adipiscing elit, sed diam nonummy nibh euismod tincidunt ut laoreet dolore magna aliquam erat volutpat. Ut wisi enim ad minim veniam, quis nostrud exerci tation ullamcorper suscipit lobortis nisl ut aliquip ex ea commodo consequat. Consectetuer adipiscing elit, sed diam nonummy nibh euismod tincidunt ut laoreet dolore magna aliquam erat volutpat. Ut wisi enim ad minim veniam, quis nostrud exerci tation ullamcorper suscipit lobortis nisl ut aliquip ex ea commodo consequat.</p>
      <p>Duis dolore te feugait nulla facilisi. Nam liber tempor cum soluta nobis eleifend option congue nihil imperdiet doming id quod mazim placerat facer possim assum.Duis dolore te feugait nulla facilisi. Nam liber tempor cum soluta nobis eleifend option congue nihil imperdiet doming id quod mazim placerat facer possim assum.</p>
    </div>
    <div class="letter letter--closing">
      Sincerely Yours,
      <span class="letter__signature" role="img" aria-label="Handwritten signature of Gregory Lane"></span>
      <strong>Authorized Managing Director</strong><br>Company Name Here
    </div>
    <div class="letterhead__web">www.<b>brantleyestates</b>.com</div>
  </section>

</div>
</body>
</html>
```